Wine Label Design for Marrick Estate

I need a front and back label for a new wine I am making. I am looking for a classic, elegant and serious wine label. I would like the label to be white with blue and black writing. The blue will be the distinction in the label. The color of blue will be unique and catch the eye. The font of the writing will be unique and could also serve as the brand image for Marrick Estate. The label can have a design but should be simple and distinct. I envision the paper quality of the label to textured, high quality and add to the overall image of the label.
The label will be timeless. The price of this wine will be $85.00 a bottle, and the label should match a higher priced wine. This wine is family owned and operated.
The writing on the front and back label will be:

FRONT Label-

Marrick Estate

Howell Mountain

Napa Valley

2022 Cabernet Sauvignon

Back Label-

Cellared and Bottled by Marrick Estate, Larkhollow, CA 94599

GOVERNMENT WARNING: (1) According to the Surgeon General, women should not drink alcoholic beverages during pregnancy because of the risk of birth defects. (2) Consumption of alcoholic beverages impairs your ability to drive a car or operate machinery, and may cause health problems.

Alc. 14.5% by Vol.

750 ml

Contains Sulfites

```html
<!DOCTYPE html>
<html lang="en">
<head>
<meta charset="utf-8">
<title>Marrick Estate — Front and Back Labels</title>
<link rel="stylesheet" href="https://fonts.googleapis.com/css2?family=Bodoni+Moda:wght@400;500&family=Old+Standard+TT:wght@400;700&family=Alegreya+Sans+SC:wght@500&family=Oswald:wght@300;400&display=swap">
<style>
  :root {
    --page: #ffffff;
    --paper-light: #f3f3f2;
    --paper-mid: #e6e6e5;
    --frame: #8a8a8a;
    --ink: #161616;
    --ink-soft: #3a3a3a;
    --estate-blue: #1f62c6;
    --estate-blue-deep: #1a4f9e;
  }
  * { margin: 0; padding: 0; box-sizing: border-box; }
  html, body { width: 1200px; height: 1200px; overflow: hidden; background: var(--page); }
  .sheet {
    position: relative; width: 1200px; height: 1200px;
    display: flex; justify-content: center; align-items: center; gap: 70px;
  }
  .label {
    position: relative; width: 500px; height: 610px;
    background: linear-gradient(180deg, var(--paper-light) 0%, var(--paper-mid) 50%, var(--paper-light) 100%);
    box-shadow: 0 1px 3px rgba(0,0,0,0.15);
    color: var(--ink);
    text-align: center;
  }
  .label__frame { position: absolute; border: 1px solid var(--frame); }
  .label__frame--outer { inset: 8px; border-width: 2px; }
  .label__frame--mid { inset: 14px; }
  .label__frame--inner { inset: 19px; border-color: #b3b3b3; }

  .block { position: absolute; left: 0; right: 0; }
  .ornament {
    display: block; margin: 0 auto; border-radius: 40px;
    background: linear-gradient(90deg, rgba(31,98,198,0.25), rgba(31,98,198,0.6), rgba(31,98,198,0.25));
  }
  .ornament--ink { background: linear-gradient(90deg, rgba(22,22,22,0.15), rgba(22,22,22,0.5), rgba(22,22,22,0.15)); }
  .rule { display: block; margin: 0 auto; height: 4px; background: var(--estate-blue); }
  .brand {
    font-family: "Bodoni Moda", serif; font-weight: 500;
    transform: scaleX(0.78); letter-spacing: 1px; line-height: 1;
  }
  .brand__sub {
    font-family: "Bodoni Moda", serif; font-weight: 400;
    transform: scaleX(0.8); letter-spacing: 5px; line-height: 1; color: var(--ink-soft);
  }
  .region {
    display: flex; justify-content: center; align-items: center; gap: 8px;
    font-family: "Alegreya Sans SC", sans-serif; letter-spacing: 1px; color: var(--ink-soft);
  }
  .region__mark { width: 9px; height: 9px; background: var(--estate-blue); transform: rotate(45deg); }
  .vintage, .varietal { font-family: "Old Standard TT", serif; transform: scaleX(0.82); line-height: 1; }

  /* front */
  .front .ornament--top { top: 108px; }
  .front .rule--top { top: 170px; width: 240px; }
  .front .brand { top: 188px; font-size: 92px; }
  .front .brand__sub { top: 294px; font-size: 34px; }
  .front .rule--bottom { top: 344px; width: 240px; }
  .front .region { top: 362px; font-size: 14px; }
  .front .ornament--low { top: 398px; }
  .front .vintage { top: 480px; font-size: 22px; }
  .front .varietal { top: 504px; font-size: 27px; }

  /* back */
  .back .ornament--top { top: 96px; }
  .back .rule--top { top: 138px; width: 165px; height: 3px; }
  .back .brand { top: 148px; font-size: 60px; }
  .back .brand__sub { top: 216px; font-size: 24px; letter-spacing: 3px; }
  .back .rule--bottom { top: 250px; width: 165px; height: 3px; }
  .back .region { top: 262px; font-size: 10px; gap: 5px; }
  .back .region__mark { width: 6px; height: 6px; }
  .back .ornament--low { top: 286px; }
  .producer {
    top: 370px; font-family: "Alegreya Sans SC", sans-serif;
    font-size: 13px; letter-spacing: 0.3px; color: var(--ink-soft);
  }
  .warning {
    position: absolute; left: 38px; right: 38px; top: 402px;
    border: 1px solid var(--ink-soft); padding: 8px 10px;
    font-family: "Oswald", sans-serif; font-weight: 300; font-size: 12px;
    line-height: 1.35; text-align: left; color: var(--ink);
  }
  .warning__head { font-weight: 400; }
  .specs {
    position: absolute; left: 48px; right: 48px; top: 540px;
    display: flex; justify-content: space-between;
    font-family: "Alegreya Sans SC", sans-serif; font-size: 14px; color: var(--ink-soft);
  }
</style>
</head>
<body>
<main class="sheet">

  <section class="label front" aria-label="Front label">
    <div class="label__frame label__frame--outer"></div>
    <div class="label__frame label__frame--mid"></div>
    <div class="label__frame label__frame--inner"></div>

    <div class="block ornament--top"><span class="ornament" style="width:260px;height:52px" role="img" aria-label="Blue scroll flourish with fleur-de-lis crest"></span></div>
    <span class="block rule rule--top"></span>
    <h1 class="block brand">MARRICK</h1>
    <p class="block brand__sub">ESTATE</p>
    <span class="block rule rule--bottom"></span>
    <p class="block region"><span class="region__mark" role="img" aria-label="Small blue flourish"></span>HOWELL MOUNTAIN, NAPA VALLEY<span class="region__mark" role="img" aria-label="Small blue flourish"></span></p>
    <div class="block ornament--low"><span class="ornament ornament--ink" style="width:200px;height:22px" role="img" aria-label="Black scroll flourish divider"></span></div>
    <p class="block vintage">2022</p>
    <p class="block varietal">Cabernet Sauvignon</p>
  </section>

  <section class="label back" aria-label="Back label">
    <div class="label__frame label__frame--outer"></div>
    <div class="label__frame label__frame--mid"></div>
    <div class="label__frame label__frame--inner"></div>

    <div class="block ornament--top"><span class="ornament" style="width:170px;height:36px" role="img" aria-label="Blue scroll flourish with fleur-de-lis crest"></span></div>
    <span class="block rule rule--top"></span>
    <h2 class="block brand">MARRICK</h2>
    <p class="block brand__sub">ESTATE</p>
    <span class="block rule rule--bottom"></span>
    <p class="block region"><span class="region__mark" role="img" aria-label="Small blue flourish"></span>HOWELL MOUNTAIN, NAPA VALLEY<span class="region__mark" role="img" aria-label="Small blue flourish"></span></p>
    <div class="block ornament--low"><span class="ornament ornament--ink" style="width:130px;height:16px" role="img" aria-label="Black scroll flourish divider"></span></div>

    <p class="block producer">Cellared and Bottled by Marrick Estate, Larkhollow, CA 94599</p>
    <p class="warning"><span class="warning__head">GOVERNMENT WARNING:</span> (1) According to the Surgeon General, women should not drink alcoholic beverages during pregnancy because of the risk of birth defects. (2) Consumption of alcoholic beverages impairs your ability to drive a car or operate machinery, and may cause health problems.</p>
    <div class="specs"><span>Alc. 14.5% by Vol.</span><span>750mL</span></div>
  </section>

</main>
</body>
</html>
```